Very High End Grooming Salon needs new business card design

I need a very nice card design I am a certified Master groomer we have a very high end clients. Our color is pink but does not have to be pink. I have a logo also a mission statement .
Fluff N Fern Pet Boutique and Spa
48810 Marlow Rd
North Palm Beach fl 33471
561 904 3782
www.fluffernboutique.example
online booking available
this is our mission statement not sure it need to go on card but here it is.
Our Mission is to show respect to all animals pampering them with the same high end tailored service one would expect to receive at a day spa
as the only certified master groomer in the area we strive to put your pets best paw forward.

Industry/Entity Type

Business

```html
<!DOCTYPE html>
<html lang="en">
<head>
<meta charset="utf-8">
<title>Fluff N Fern Pet Boutique and Spa – Business Card</title>
<link rel="stylesheet" href="https://fonts.googleapis.com/css2?family=Open+Sans:wght@400;600&display=swap">
<style>
  :root {
    --canvas: #ffffff;
    --card-white: #ffffff;
    --card-edge: #e4e4e4;
    --magenta: #d6108d;
    --hot-pink: #e2168c;
    --berry: #c0167c;
    --wine: #7a1444;
    --blush: #f7b8d8;
    --soft-pink: #f5a3cf;
    --text-light: #ffffff;
  }
  * { box-sizing: border-box; margin: 0; padding: 0; }
  html, body {
    width: 1200px; height: 800px; overflow: hidden;
    background: var(--canvas);
    font-family: "Open Sans", Arial, sans-serif;
  }
  .canvas { position: relative; width: 1200px; height: 800px; }
  .card {
    position: absolute; top: 100px;
    width: 329px; height: 594px;
    border-radius: 24px;
    box-shadow: 8px 12px 18px rgba(0,0,0,0.22);
    text-align: center;
  }
  .card--front { left: 241px; background: var(--card-white); border: 1px solid var(--card-edge); }
  .card--back { left: 630px; background: var(--magenta); }

  .brand-name {
    position: absolute; top: 36px; left: 0; right: 0;
    font-size: 27px; font-weight: 400; color: var(--berry);
  }
  .brand-mark {
    position: absolute; top: 86px; left: 50%;
    width: 170px; height: 170px; margin-left: -85px;
    border-radius: 50%; background: var(--blush);
  }
  .brand-tagline {
    position: absolute; top: 272px; left: 0; right: 0;
    font-size: 13px; letter-spacing: 1.5px; text-transform: uppercase;
    color: var(--berry);
  }
  .divider-ornament {
    position: absolute; top: 317px; left: 50%;
    width: 116px; height: 20px; margin-left: -58px;
    border-radius: 10px;
    background: linear-gradient(90deg, var(--wine), var(--soft-pink), var(--wine));
  }
  .address {
    position: absolute; top: 375px; left: 0; right: 0;
    font-size: 18.5px; line-height: 23px; color: var(--berry); font-style: normal;
  }
  .phone {
    position: absolute; top: 462px; left: 0; right: 0;
    font-size: 23px; font-weight: 600; color: var(--hot-pink); letter-spacing: 0.5px;
  }
  .web {
    position: absolute; top: 512px; left: 0; right: 0;
    font-size: 17px; font-weight: 600; color: var(--wine); line-height: 20px;
  }
  .web small { display: block; font-size: 13px; font-weight: 400; line-height: 16px; }

  .swirl-art {
    position: absolute; top: 34px; left: 38px;
    width: 258px; height: 320px;
    border-radius: 120px 120px 40px 120px;
    background: radial-gradient(circle at 55% 35%, #ffffff 0%, var(--blush) 40%, #ee4fb0 70%, var(--wine) 100%);
    opacity: 0.9;
  }
  .mission {
    position: absolute; left: 22px; right: 22px;
    font-size: 15.5px; line-height: 19.5px; color: var(--text-light);
  }
  .mission--statement { top: 370px; }
  .mission--promise { top: 506px; }
</style>
</head>
<body>
<main class="canvas">
  <section class="card card--front" aria-label="Card front">
    <h1 class="brand-name">Fluff N Fern</h1>
    <div class="brand-mark" aria-hidden="true"></div>
    <p class="brand-tagline">Pet Boutique and Spa</p>
    <div class="divider-ornament" role="img" aria-label="Decorative swirl divider"></div>
    <address class="address">
      Fluff N Fern Pet Boutique and Spa<br>
      48810 Marlow Rd<br>
      North Palm Beach fl 33471
    </address>
    <p class="phone">561 904 3782</p>
    <p class="web">www.fluffernboutique.example<small>online booking available</small></p>
  </section>

  <section class="card card--back" aria-label="Card back">
    <div class="swirl-art" role="img" aria-label="Decorative pink and white flowing swirl illustration"></div>
    <p class="mission mission--statement">Our Mission is to show respect to all animals pampering them with the same high end tailored service one would expect to receive at a day spa.</p>
    <p class="mission mission--promise">As the only certified master groomer in the area we strive to put your pets best paw forward.</p>
  </section>
</main>
</body>
</html>
```